Web page design for podiatry office*

Need a web page for our podiatry office. It should feature most of our services, hours, directions and location. Should include a short bio of the doctor and a contact page.

Coding

Coded - Design and coding required

Number of Pages Required

1 page

Colors

Designer to choose colors to be used in the design.

```html
<!DOCTYPE html>
<html lang="en">
<head>
<meta charset="utf-8">
<title>Podiatry Office</title>
<link href="https://fonts.googleapis.com/css2?family=Mulish:wght@400;600;700;800&family=Yellowtail&display=swap" rel="stylesheet">
<style>
:root{
  --teal:#0a819c;
  --teal-dark:#066b82;
  --orange:#f4623a;
  --ink:#333;
  --muted:#5b5b5b;
  --pale:#eef5f8;
  --wave:#bfe0ea;
  --field:#f6f6f6;
  --line:#e3e3e3;
  --white:#fff;
}
*{margin:0;padding:0;box-sizing:border-box}
html,body{width:1200px;height:3203px;overflow:hidden}
body{position:relative;font-family:"Mulish",sans-serif;color:var(--ink);background:var(--white)}
.abs{position:absolute}
.topbar{left:0;top:0;width:1200px;height:41px;background:var(--teal);color:var(--white)}
.topbar .label{right:250px;top:11px;font-size:15px}
.topbar .phone-ico{right:210px;top:6px;width:29px;height:29px;border-radius:50%;background:var(--orange)}
.topbar .number{right:77px;top:8px;font-size:19px;font-weight:800}
.brand{left:77px;top:70px;font-size:28px;font-weight:800;line-height:32px;color:var(--teal);text-align:center;width:142px}
.nav{left:483px;top:70px;display:flex;gap:26px;font-size:16px;font-weight:600;color:var(--ink)}
.nav .active{color:var(--orange)}
.search{left:842px;top:60px;width:280px;height:39px;border:1px solid var(--line);border-radius:20px;background:var(--white);font-size:12px;color:#999;padding:11px 18px}
.search svg{position:absolute;right:14px;top:11px}
.hero{left:0;top:0}
.hero-text{left:78px;top:268px;color:var(--white)}
.hero-text .script{font-family:"Yellowtail",cursive;font-size:46px;line-height:1}
.hero-text h1{font-size:62px;font-weight:800;line-height:1;margin-top:6px;letter-spacing:.5px}
.hero-text p{font-size:18px;line-height:28px;margin-top:14px;width:420px}
.btn{display:inline-block;background:var(--orange);color:var(--white);font-weight:800;border-radius:30px;text-align:center}
.hero .btn{position:absolute;left:78px;top:469px;width:291px;height:51px;line-height:51px;font-size:18px}
.dot{left:1154px;width:15px;height:15px;border-radius:50%;border:1.5px solid var(--white)}
.dot.on{background:var(--orange);border-color:var(--orange)}
.welcome{left:0;top:770px;width:1200px;text-align:center}
.welcome .eyebrow{font-size:18px;font-weight:700;color:var(--orange)}
.welcome h2{font-size:42px;font-weight:800;color:var(--teal);margin-top:6px}
.welcome p{width:640px;margin:14px auto 0;font-size:15px;line-height:27px;color:var(--muted)}
.card{top:989px;width:323px;height:410px;background:var(--teal);color:var(--white);overflow:hidden}
.card svg{position:absolute;left:0;top:0}
.card h3{position:absolute;left:21px;top:250px;font-size:18px;font-weight:800;letter-spacing:.2px}
.card p{position:absolute;left:23px;top:290px;width:285px;font-size:14.5px;line-height:27.5px}
.bio-photo{left:145px;top:1469px;width:386px;height:458px;background:linear-gradient(180deg,#7b7b7b,#5d5d5d 60%,#c9c9c9)}
.bio-text{left:637px;top:1565px;color:var(--white);width:430px}
.bio-text h2{font-size:44px;font-weight:800}
.bio-text p{font-size:14.5px;line-height:27px;margin-top:20px;margin-left:6px}
.bio-text p+p{margin-top:15px}
.bio-btn{left:639px;top:1861px;width:172px;height:55px;line-height:55px;font-size:19px;font-weight:600}
.standards{left:0;top:1991px;width:1200px;height:140px;background:var(--teal);color:var(--white);text-align:center}
.standards p{font-size:18px;margin-top:33px}
.standards h2{font-size:42px;font-weight:800;margin-top:2px}
.notch{left:580px;top:2130px}
.info{left:0;top:2131px;width:1200px;height:500px;background:var(--pale)}
.info-item{top:2214px;width:320px;text-align:center}
.info-item .ring{width:78px;height:78px;margin:0 auto;border-radius:50%;border:2px dotted #9ccbd8;padding:6px}
.info-item .disc{width:62px;height:62px;border-radius:50%;background:var(--teal);display:flex;align-items:center;justify-content:center}
.info-item .disc.alt{background:var(--orange)}
.info-item h3{font-size:19px;font-weight:800;color:var(--teal);margin-top:29px}
.info-item .bar{width:22px;height:2px;background:var(--teal);margin:9px auto 0}
.info-item p{font-size:13.5px;line-height:27px;color:var(--muted);margin-top:16px}
.info-item .closed{color:var(--orange)}
.connector{top:2254px;height:0;border-top:1.5px dotted #9ccbd8}
.book-head{left:137px;top:2694px}
.book-head .eyebrow{font-size:18px;font-weight:800;color:var(--orange)}
.book-head h2{font-size:44px;line-height:47px;font-weight:800;color:var(--teal);margin-top:10px}
.field{left:536px;width:287px;height:47px;background:var(--field);border:1px solid var(--line);font-size:14.5px;color:#777;padding:13px 15px}
.field.msg{left:837px;top:2652px;width:286px;height:161px}
.send{left:536px;top:2825px;width:140px;height:50px;line-height:50px;font-size:18px}
.footer{left:0;top:2937px;width:1200px;height:266px;background:var(--teal);color:var(--white);text-align:center}
.footer .name{font-size:28px;font-weight:800;margin-top:50px}
.social{display:flex;justify-content:center;gap:10px;margin-top:17px}
.social span{width:40px;height:40px;border-radius:50%;background:var(--white);display:block}
.footer .links{font-size:15px;margin-top:22px}
.footer .copy{font-size:13px;margin-top:12px}
</style>
</head>
<body>

<svg class="abs hero-bg" style="left:0;top:0" width="1200" height="730" viewBox="0 0 1200 730">
  <defs>
    <linearGradient id="heroTone" x1="0" y1="0" x2="1" y2="1">
      <stop offset="0" stop-color="#3f6a63"/>
      <stop offset=".5" stop-color="#566b6c"/>
      <stop offset="1" stop-color="#2f4a55"/>
    </linearGradient>
    <linearGradient id="headFade" x1="0" y1="0" x2="0" y2="1">
      <stop offset="0" stop-color="#fff"/>
      <stop offset=".7" stop-color="#fff" stop-opacity=".85"/>
      <stop offset="1" stop-color="#e5f0f3"/>
    </linearGradient>
  </defs>
  <path d="M0 199 C300 150 550 120 1200 116 L1200 590 C900 640 600 720 330 715 C180 712 80 690 0 656 Z" fill="url(#heroTone)" role="img" aria-label="Photo of a runner on an open road"/>
  <path d="M0 650 C80 688 180 706 330 709 C600 714 900 640 1200 583 L1200 596 C900 655 600 725 330 722 C170 720 70 700 0 668 Z" fill="var(--teal)"/>
  <path d="M0 41 L1200 41 L1200 116 C550 120 300 150 0 199 Z" fill="url(#headFade)"/>
</svg>

<div class="abs topbar">
  <span class="abs label">Book An Appointment :</span>
  <span class="abs phone-ico">
    <svg width="29" height="29" viewBox="0 0 29 29"><path d="M10 8c1 0 2 3 2 4s-1 1-1 2 2 4 4 4 1-1 2-1 4 1 4 2-1 3-3 3c-5 0-10-5-10-10 0-2 1-4 2-4z" fill="#fff"/></svg>
  </span>
  <span class="abs number">123 456 7890</span>
</div>

<div class="abs brand">PODIATRY<br>OFFICE</div>
<nav class="abs nav"><span class="active">HOME</span><span>BIO</span><span>SERVICES</span><span>CONTACT US</span></nav>
<div class="abs search">Type Here...
  <svg width="16" height="16" viewBox="0 0 16 16"><circle cx="6.5" cy="6.5" r="4.5" fill="none" stroke="#f4623a" stroke-width="2"/><path d="M10 10l4 4" stroke="#f4623a" stroke-width="2.4" stroke-linecap="round"/></svg>
</div>

<div class="abs hero">
  <div class="abs hero-text">
    <div class="script">Your Next</div>
    <h1>Step Forward</h1>
    <p>Lorem Ipsum is simply dummy text of the printing and typesetting industry. Lorem Ipsum has been</p>
  </div>
  <span class="btn">BOOK AN APPOINTMENT</span>
</div>
<span class="abs dot" style="top:306px"></span>
<span class="abs dot" style="top:330px"></span>
<span class="abs dot" style="top:354px"></span>
<span class="abs dot on" style="top:378px"></span>
<span class="abs dot" style="top:402px"></span>

<section class="abs welcome">
  <div class="eyebrow">WELCOME TO</div>
  <h2>PODIATRY OFFICE</h2>
  <p>Lorem Ipsum is simply dummy text of the printing and the typesetting industry. Lorem Ipsum has been the industry's standard dummy text ever since the 1500s, when an unkno printer took a galley of type and scrambled it.</p>
</section>

<article class="abs card" style="left:94px">
  <svg width="323" height="215" viewBox="0 0 323 215">
    <rect width="323" height="215" fill="#d9b8a2" role="img" aria-label="Photo of a foot being examined"/>
    <path d="M0 185 C110 180 220 190 323 215 L323 215 L0 215 Z" fill="var(--teal)"/>
    <path d="M0 179 C110 174 220 184 323 205 L323 215 C220 192 110 184 0 187 Z" fill="var(--orange)"/>
  </svg>
  <h3>GENERAL TREATMENT</h3>
  <p>Lorem Ipsum is simply dummy text of the printing and the typesetting Lorem Ipsum has been the industry.</p>
</article>
<article class="abs card" style="left:439px">
  <svg width="323" height="215" viewBox="0 0 323 215">
    <rect width="323" height="215" fill="#e8d5c8" role="img" aria-label="Photo of a specialist treating a foot"/>
    <path d="M0 185 C110 180 220 190 323 215 L0 215 Z" fill="var(--teal)"/>
    <path d="M0 179 C110 174 220 184 323 205 L323 215 C220 192 110 184 0 187 Z" fill="#fff"/>
  </svg>
  <h3>SPECIALISED TREATMENT</h3>
  <p>Lorem Ipsum is simply dummy text of the printing and the typesetting Lorem Ipsum has been the industry.</p>
</article>
<article class="abs card" style="left:782px">
  <svg width="323" height="215" viewBox="0 0 323 215">
    <rect width="323" height="215" fill="#b9c3c8" role="img" aria-label="Photo of a runner's feet on a treadmill"/>
    <path d="M0 185 C110 180 220 190 323 215 L0 215 Z" fill="var(--teal)"/>
    <path d="M0 179 C110 174 220 184 323 205 L323 215 C220 192 110 184 0 187 Z" fill="#fff"/>
  </svg>
  <h3>SPORTS INJURY</h3>
  <p>Lorem Ipsum is simply dummy text of the printing and the typesetting Lorem Ipsum has been the industry.</p>
</article>

<svg class="abs" style="left:0;top:1480px" width="1200" height="512" viewBox="0 0 1200 512">
  <defs>
    <linearGradient id="bioTone" x1="0" y1="0" x2="1" y2="0">
      <stop offset="0" stop-color="#2f8a95"/>
      <stop offset=".5" stop-color="#4b6c6c"/>
      <stop offset="1" stop-color="#3b4c50"/>
    </linearGradient>
  </defs>
  <path d="M0 108 C400 80 800 0 1200 4 L1200 512 L0 512 Z" fill="url(#bioTone)" role="img" aria-label="Faded photo of an open road"/>
</svg>
<div class="abs bio-photo" role="img" aria-label="Portrait photo of the doctor"></div>
<div class="abs bio-text">
  <h2>BIO</h2>
  <p>Lorem Ipsum is simply dummy text of the printing and typesetting industry. Lorem Ipsum has been the industry's standard dummy text ever since the 1500s</p>
  <p>Lorem Ipsum is simply dummy text of the printing and the typesetting industry. Lorem Ipsum has been the industry's standard dummy text ever since the 1500s, when an unkno printer took a galley of type and scrambled i.</p>
</div>
<span class="abs btn bio-btn">LEARN MORE</span>

<section class="abs standards">
  <p>Setting the Standards for</p>
  <h2>QUALITY PATIENT CARE</h2>
</section>
<div class="abs info"></div>
<svg class="abs notch" width="40" height="20" viewBox="0 0 40 20"><path d="M0 0 L40 0 L20 20 Z" fill="var(--teal)"/></svg>

<span class="abs connector" style="left:307px;width:254px"></span>
<span class="abs connector" style="left:637px;width:258px"></span>

<div class="abs info-item" style="left:109px">
  <div class="ring"><div class="disc">
    <svg width="30" height="30" viewBox="0 0 30 30"><circle cx="15" cy="15" r="11" fill="none" stroke="#fff" stroke-width="2.2"/><path d="M15 9v6l4 3" fill="none" stroke="#fff" stroke-width="2.2" stroke-linecap="round"/></svg>
  </div></div>
  <h3>HOURS</h3><div class="bar"></div>
  <p>Mon-Sat : 9am to 5pm<br>Sunday : <span class="closed">Closed</span></p>
</div>
<div class="abs info-item" style="left:439px">
  <div class="ring"><div class="disc alt">
    <svg width="30" height="30" viewBox="0 0 30 30"><path d="M14 4h2v22h-2z" fill="#fff"/><path d="M6 8h16l3 3-3 3H6z M24 16H8l-3 3 3 3h16z" fill="#fff"/></svg>
  </div></div>
  <h3>DIRECTIONS</h3><div class="bar"></div>
  <p>101 - Lorem ipsum the simple text of<br>print typesetting industry.</p>
</div>
<div class="abs info-item" style="left:773px">
  <div class="ring"><div class="disc">
    <svg width="30" height="30" viewBox="0 0 30 30"><path d="M15 3c-5 0-9 4-9 9 0 6 9 15 9 15s9-9 9-15c0-5-4-9-9-9z" fill="none" stroke="#fff" stroke-width="2.4"/><circle cx="15" cy="12" r="3.2" fill="#fff"/></svg>
  </div></div>
  <h3>LOCATION</h3><div class="bar"></div>
  <p>101 - Lorem ipsum the simple text of<br>print typesetting industry.</p>
</div>

<svg class="abs" style="left:0;top:2440px" width="1200" height="200" viewBox="0 0 1200 200">
  <path d="M0 50 C300 90 700 60 1200 10 L1200 200 L0 200 Z" fill="#d7ebf1"/>
  <path d="M0 60 C400 110 800 60 1200 40 L1200 200 L0 200 Z" fill="var(--wave)"/>
  <path d="M0 180 C300 150 600 120 900 110 C1000 106 1100 100 1200 92 L1200 200 L0 200 Z" fill="#fff"/>
</svg>

<div class="abs book-head">
  <div class="eyebrow">PODIATRY OFFICE</div>
  <h2>BOOK AN<br>APPOINTMENT</h2>
</div>
<div class="abs field" style="top:2652px">Name *</div>
<div class="abs field" style="top:2710px">Email *</div>
<div class="abs field" style="top:2767px">Services*</div>
<div class="abs field msg">Message *</div>
<span class="abs btn send">SEND US</span>

<footer class="abs footer">
  <div class="name">PODIATRY OFFICE</div>
  <div class="social"><span aria-label="Professional network"></span><span aria-label="Social page"></span><span aria-label="Microblog"></span></div>
  <div class="links">Home | Bio | Services | Contact</div>
  <div class="copy">©PODIATRY OFFICE - 2019 All Rights Reserved.</div>
</footer>

</body>
</html>
```